Design for Cedar Lark Homes real estate agency

Incorporate logo into new business cards. I need to include the Brindley Vance logo incorporated into Cedar Lark Homes on one side of the card (attached). On the other side I see just the icon with "Maren Quill" (attached) with "Connected by Trust" either included as is or removed from logo and rather put as a tag line on the business card separate from the main logo. Contact information:

Maren Quill
Associate Broker
Cell: 730-418-5093
Email: marenquill@cedarlarkhomes.example
Web: www.cedarlarkhomes.example

Target Market(s)

Buyers, Sellers, Builders and Investors of homes and land

Industry/Entity Type

Real Estate Agent

Contact Information for Business Card

My client base tend to be higher end home buyers, sellers, builders and investors. I have been more and more in land and subdivisions for builders and investors. The card should not be cluttered. Clean and simple - yet with an air of exclusive/high end

Colors

Designer to choose colors to be used in the design.

Requirements
Must have
• Must have the logo on one side that has Brindley Vance logo incorporated. The side that has my contact information does not have to have the Brindley Vance logo incorporated.
• Must include "Connected by Trust" tag line either within logo (as is) or removed from logo and included in another position on the side of the business card with contact information.
Should not have
• Should not have Brindley Vance logo incorporated into Cedar Lark Homes logo on both sides of business card. Would like the Cedar Lark Homes logo that has Brindley Logo only on the back side of card without contact information.

```html
<!DOCTYPE html>
<html lang="en">
<head>
<meta charset="utf-8">
<title>Cedar Lark Homes – Maren Quill Business Card</title>
<link href="https://fonts.googleapis.com/css2?family=Cinzel:wght@500;600&family=Cormorant+Garamond:wght@600&family=Montserrat:wght@400&family=Poppins:wght@400&display=swap" rel="stylesheet">
<style>
  :root {
    --bg: #2b2b2d;
    --brown: #5e4120;
    --brown-light: #6e4f2d;
    --gold: #c9a42c;
    --white: #ffffff;
    --ink: #3a3a3a;
    --faint: #e6e6e6;
  }
  * { margin: 0; padding: 0; box-sizing: border-box; }
  html, body { width: 1200px; height: 900px; overflow: hidden; background: var(--bg); }
  .canvas {
    width: 1200px; height: 900px;
    display: flex; flex-direction: column; align-items: center; justify-content: center; gap: 24px;
  }
  .card { position: relative; width: 735px; height: 420px; overflow: hidden; box-shadow: 0 14px 30px rgba(0,0,0,.45); }

  /* Back side */
  .card--back { background: linear-gradient(100deg, var(--brown) 0%, var(--brown-light) 100%); color: var(--white); }
  .world-map {
    position: absolute; left: 120px; top: 50px; width: 520px; height: 300px;
    background: radial-gradient(ellipse at center, rgba(255,255,255,.08) 0%, rgba(255,255,255,0) 70%);
  }
  .brand { position: absolute; left: 95px; top: 125px; width: 560px; }
  .brand__row { display: flex; align-items: center; gap: 18px; }
  .brand__mark { width: 62px; height: 62px; border-radius: 50%; background: var(--white); flex: none; }
  .brand__name { font-family: "Cormorant Garamond", serif; font-weight: 600; font-size: 46px; letter-spacing: .5px; line-height: 1; }
  .brand__agent { display: flex; align-items: center; gap: 10px; margin: 12px 0 0 80px; }
  .brand__rule { height: 1px; background: var(--white); flex: 1; }
  .brand__agent-name { font-family: "Cinzel", serif; font-weight: 600; font-size: 17px; letter-spacing: 4px; }
  .brand__tagline { font-family: "Montserrat", sans-serif; font-size: 9px; letter-spacing: 5px; margin: 4px 0 0 190px; }
  .partner { position: absolute; right: 60px; top: 228px; display: flex; align-items: center; gap: 8px; }
  .partner__square { width: 16px; height: 16px; background: var(--white); }
  .partner__name { font-family: "Cormorant Garamond", serif; font-weight: 600; font-size: 16px; }
  .partner__sub { position: absolute; right: 60px; top: 252px; font-family: "Cormorant Garamond", serif; font-weight: 600; font-size: 8px; letter-spacing: 1px; text-transform: uppercase; }

  /* Front side */
  .card--front { background: var(--white); }
  .front__title { position: absolute; left: 62px; top: 40px; font-family: "Cinzel", serif; font-weight: 600; font-size: 46px; letter-spacing: 8px; color: var(--brown); }
  .front__tagline { position: absolute; left: 68px; top: 104px; font-family: "Montserrat", sans-serif; font-size: 12px; letter-spacing: 6px; color: var(--brown); text-transform: uppercase; }
  .front__name { position: absolute; left: 70px; top: 160px; font-family: "Cinzel", serif; font-weight: 600; font-size: 21px; color: var(--brown); }
  .front__role { position: absolute; left: 70px; top: 190px; font-family: "Cinzel", serif; font-weight: 500; font-size: 15px; color: var(--ink); }
  .contact { position: absolute; left: 70px; top: 232px; list-style: none; font-family: "Poppins", sans-serif; font-size: 16px; color: var(--ink); }
  .contact li { display: flex; align-items: center; gap: 14px; height: 28px; }
  .contact svg { width: 16px; height: 16px; flex: none; }
  .contact .accent { color: var(--gold); }
  .emblem { position: absolute; left: 470px; top: 110px; width: 200px; text-align: center; }
  .emblem__circle { width: 170px; height: 170px; margin: 0 auto; border-radius: 50%; background: var(--faint); }
  .emblem__name { margin-top: 8px; font-family: "Cormorant Garamond", serif; font-weight: 600; font-size: 20px; color: var(--faint); }
  .waves { position: absolute; left: 0; top: 0; width: 735px; height: 420px; }
</style>
</head>
<body>
<main class="canvas">
  <section class="card card--back" aria-label="Card back">
    <div class="world-map" role="img" aria-label="Faint dotted world map"></div>
    <div class="brand">
      <div class="brand__row">
        <span class="brand__mark"></span>
        <span class="brand__name">Cedar Lark Homes</span>
      </div>
      <div class="brand__agent">
        <span class="brand__rule"></span>
        <span class="brand__agent-name">MAREN QUILL</span>
        <span class="brand__rule" style="flex:0 0 40px"></span>
      </div>
      <div class="brand__tagline">CONNECTED BY TRUST</div>
    </div>
    <div class="partner">
      <span class="partner__square"></span>
      <span class="partner__name">Brindley Vance</span>
    </div>
    <div class="partner__sub">Residential Brokerage</div>
  </section>

  <section class="card card--front" aria-label="Card front">
    <div class="emblem">
      <div class="emblem__circle"></div>
      <div class="emblem__name">Cedar Lark Homes</div>
    </div>
    <h1 class="front__title">MAREN QUILL</h1>
    <p class="front__tagline">Connected by Trust</p>
    <p class="front__name">MAREN QUILL</p>
    <p class="front__role">ASSOCIATE BROKER</p>
    <ul class="contact">
      <li>
        <svg viewBox="0 0 16 16"><rect x="4" y="1" width="8" height="14" rx="1.5" fill="none" stroke="var(--gold)" stroke-width="1.4"/></svg>
        730-418-5093
      </li>
      <li>
        <svg viewBox="0 0 16 16"><rect x="1" y="3" width="14" height="10" fill="var(--gold)"/><path d="M1 3 L8 9 L15 3" fill="none" stroke="var(--white)" stroke-width="1.2"/></svg>
        marenquill@cedarlarkhomes.example
      </li>
      <li>
        <svg viewBox="0 0 16 16" fill="none" stroke="var(--gold)" stroke-width="1.2"><circle cx="8" cy="8" r="6.5"/><ellipse cx="8" cy="8" rx="3" ry="6.5"/><path d="M1.5 8h13M3 4.5h10M3 11.5h10"/></svg>
        <span>www.<span class="accent">cedarlarkhomes</span>.example</span>
      </li>
    </ul>
    <svg class="waves" viewBox="0 0 735 420" aria-hidden="true">
      <path d="M0 325 C160 405 360 392 520 366 C620 350 700 356 735 370 L735 420 L0 420 Z" fill="var(--gold)"/>
      <path d="M0 340 C160 416 360 400 520 374 C620 358 700 364 735 378 L735 420 L0 420 Z" fill="var(--white)"/>
      <path d="M0 348 C160 422 360 406 520 382 C620 368 700 376 735 392 L735 420 L0 420 Z" fill="var(--brown)"/>
    </svg>
  </section>
</main>
</body>
</html>
```